Plumbing & Heating company

A leaflet containing -

Company name - Brackenfold Plumbing Solutions
logo
Mobile number - 07700 914226
Landline - 01632 870512
Email - Info@brackenfoldplumbing.example.co.uk
website - Brackenfold-plumbing.example.co.uk
Social media logos - pixgram, Chatterly

services we offer

- Boiler replacements (free quote)
- General plumbing & heating
- Tap replacements
- 1st & 2nd
- New builds & Extensions
- Cylinder replcemets

```html
<!DOCTYPE html>
<html lang="en">
<head>
<meta charset="utf-8">
<title>Brackenfold Plumbing Solutions – Leaflet</title>
<link rel="stylesheet" href="https://fonts.googleapis.com/css2?family=Montserrat:ital,wght@0,700;0,800;1,700;1,800&family=Oswald:wght@500;600&display=swap">
<style>
  :root {
    --orange: #f26b21;
    --blue: #1a6fb5;
    --white: #ffffff;
    --wood-light: #d9b98f;
    --wood-dark: #a9885f;
    --copper: #c98a5a;
    --tile: #e9e7e3;
  }
  * { margin: 0; padding: 0; box-sizing: border-box; }
  html, body { width: 848px; height: 1200px; overflow: hidden; background: var(--white); }
  .leaflet { position: relative; width: 848px; height: 1200px; overflow: hidden; background: var(--white); font-family: "Montserrat", sans-serif; }
  .backdrop { position: absolute; inset: 0; }

  .brand-disc {
    position: absolute; left: 35px; top: 22px; width: 300px; height: 300px;
    border-radius: 50%; background: var(--white);
    display: flex; flex-direction: column; align-items: center; justify-content: center;
    text-align: center; color: var(--blue); font-weight: 800; line-height: 1.15;
  }
  .brand-disc .brand-name { font-size: 30px; letter-spacing: 0.5px; }
  .brand-disc .brand-sub { font-size: 15px; letter-spacing: 1px; }

  .social { position: absolute; right: 24px; display: flex; align-items: center; gap: 10px; }
  .social span { color: var(--white); font-size: 12px; font-weight: 700; }
  .social i { display: block; width: 44px; height: 44px; border-radius: 10px; background: var(--white); }
  .social.pixgram { top: 34px; }
  .social.chatterly { top: 102px; }

  .photo { position: absolute; border: 5px solid var(--white); }
  .photo.cupboard { left: 328px; top: 28px; width: 345px; height: 615px; border-radius: 60px 24px 60px 24px;
    background: linear-gradient(160deg, var(--wood-light), var(--wood-dark)); }
  .photo.cylinder { left: 76px; top: 268px; width: 284px; height: 490px; border-radius: 50px 20px 50px 20px;
    background: linear-gradient(120deg, #f4f4f2, var(--tile) 60%, #cfcac2); }
  .photo.pipework { left: 40px; top: 732px; width: 256px; height: 430px; border-radius: 20px 40px 20px 50px;
    background: linear-gradient(150deg, #cdbfa8, var(--copper) 55%, #9a8b76); }

  .contact { position: absolute; left: 360px; top: 628px; width: 460px; text-align: center; }
  .call-now { color: var(--blue); font-style: italic; font-weight: 800; font-size: 40px; line-height: 1; }
  .phone { color: var(--orange); font-weight: 800; font-size: 45px; line-height: 1; margin-top: 16px; letter-spacing: 1px; }
  .web { font-family: "Oswald", sans-serif; color: var(--blue); font-weight: 600; font-size: 21px; line-height: 1.45; }
  .web.first { margin-top: 22px; }

  .services { position: absolute; left: 378px; top: 915px; color: var(--white); font-style: italic; font-weight: 800; }
  .services h2 { font-size: 21px; font-weight: 800; letter-spacing: 0.5px; margin-bottom: 24px; }
  .services ul { list-style: none; }
  .services li { position: relative; font-size: 23px; line-height: 34px; padding-left: 18px; }
  .services li::before { content: ""; position: absolute; left: -4px; top: 12px; width: 11px; height: 11px; border-radius: 50%; background: var(--white); }
  .services li small { font-size: 17px; font-weight: 700; }
</style>
</head>
<body>
<main class="leaflet">
  <svg class="backdrop" width="848" height="1200" viewBox="0 0 848 1200" aria-hidden="true">
    <polygon points="600,0 848,0 848,330" fill="var(--blue)"/>
    <polygon points="848,205 848,310 700,530 700,425" fill="var(--orange)"/>
    <polygon points="740,470 760,440 760,520 740,550" fill="var(--blue)"/>
    <polygon points="710,490 730,460 730,560 710,590" fill="var(--orange)"/>
    <polygon points="0,120 70,120 70,1010 0,1080" fill="var(--blue)"/>
    <polygon points="0,1080 70,1010 70,1200 0,1200" fill="var(--orange)"/>
    <path d="M18,190 A172,172 0 0 1 250,10" fill="none" stroke="var(--orange)" stroke-width="22"/>
    <path d="M270,18 A172,172 0 0 1 340,120" fill="none" stroke="var(--blue)" stroke-width="10"/>
    <path d="M408,892 L848,892 L848,1200 L330,1200 L370,925 Q375,892 408,892 Z" fill="var(--orange)"/>
  </svg>

  <div class="brand-disc">
    <div class="brand-name">BRACKENFOLD</div>
    <div class="brand-sub">PLUMBING SOLUTIONS</div>
  </div>

  <div class="social pixgram"><span>pixgram</span><i></i></div>
  <div class="social chatterly"><span>Chatterly</span><i></i></div>

  <div class="photo cupboard" role="img" aria-label="Photo of a wall-hung boiler and pipework fitted in a plywood-lined cupboard"></div>
  <div class="photo cylinder" role="img" aria-label="Photo of a hot water cylinder beside a boiler with copper pipework"></div>
  <div class="photo pipework" role="img" aria-label="Photo of copper pipe runs laid between floor joists"></div>

  <section class="contact">
    <div class="call-now">CALL NOW!</div>
    <div class="phone">M- 07700 914226</div>
    <div class="phone">L- 01632 870512</div>
    <div class="web first">Email - Info@brackenfoldplumbing.example.co.uk</div>
    <div class="web">website - Brackenfold-plumbing.example.co.uk</div>
  </section>

  <section class="services">
    <h2>SERVICES WE OFFER</h2>
    <ul>
      <li>Boiler replacements <small>(free quote)</small></li>
      <li>General plumbing &amp; heating</li>
      <li>Tap replacements</li>
      <li>1st &amp; 2nd</li>
      <li>New builds &amp; Extensions</li>
      <li>Cylinder replcemets</li>
    </ul>
  </section>
</main>
</body>
</html>
```